PostCard Design Project

We are a landscaping business and offer Landscaping services: Design • Paving and Concreting styles • Pool Copings • Retaining Walls • Plant Supply • Decking • Pergolas • Water Features • Irrigation • Instant Turf • Synthetic Turf Surfaces • and more...

We are looking to create a Postcard - this will be used when we are working on a project and will be dropped into letterboxes of the residents neighbouring the project address. It should be along the lines of: "We apologise for any disturbance you may incur while we are working on your neighbours property." It should also include a 10% discount offer for any services they would like to get done, maybe on the back,, along the lines of" While we are in your area we'd like to offer you a 10% discount on any of our landscaping services" Offer valid for 30 days only. Also maybe a list of servcies on the back as well.

Industry/Entity Type

Landscaping

Requirements
Must have
• Company Logo, and contact details

```html
<!DOCTYPE html>
<html lang="en">
<head>
<meta charset="utf-8">
<title>Fernvale Landscapes – Neighbour Postcard</title>
<link rel="stylesheet" href="https://fonts.googleapis.com/css2?family=Open+Sans:wght@400;600;700&display=swap">
<style>
  :root {
    --canvas: #e9e6e1;
    --card-black: #0b0b0b;
    --leaf-green: #8cd23c;
    --band-light: #9be04a;
    --band-dark: #3f8a12;
    --band-text: #173a05;
    --photo-deep: #2f5a1f;
    --photo-mid: #5f9a34;
    --photo-light: #a9d468;
  }
  * { margin: 0; padding: 0; box-sizing: border-box; }
  html, body {
    width: 1200px; height: 900px; overflow: hidden;
    background: var(--canvas);
    font-family: "Open Sans", sans-serif;
  }
  .stage { position: relative; width: 1200px; height: 900px; }
  .postcard {
    position: absolute; top: 110px;
    width: 420px; height: 680px;
    background: var(--card-black);
    box-shadow: 0 10px 28px rgba(0,0,0,.28);
    overflow: hidden;
  }
  .postcard--front { left: 150px; }
  .postcard--back { left: 630px; }

  /* Brand */
  .brand {
    display: flex; align-items: center; gap: 10px;
    color: var(--leaf-green); font-weight: 700;
  }
  .brand__dot {
    width: 22px; height: 22px; border-radius: 50%;
    background: var(--leaf-green); flex: none;
  }
  .brand__name { font-size: 26px; line-height: 1.05; }

  /* Front */
  .front-header {
    height: 110px; padding: 22px 24px 0;
    display: flex; justify-content: space-between;
  }
  .contact {
    color: var(--leaf-green); font-size: 15px; line-height: 1.3;
    padding-top: 4px;
  }
  .rule { height: 3px; background: var(--leaf-green); margin: 0 18px; }
  .photo-grid {
    margin: 10px 18px 0;
    height: 440px;
    display: grid;
    grid-template-columns: 1fr 1fr;
    grid-template-rows: repeat(3, 1fr);
    gap: 7px;
  }
  .photo { border-radius: 1px; }
  .photo--garden { background: linear-gradient(160deg, #6b9c5a, var(--photo-mid) 55%, #c84a5a 90%); }
  .photo--trees { background: linear-gradient(170deg, #b9c6c6, #3f6b2c 40%, #7a3f58 80%); }
  .photo--steps { background: linear-gradient(150deg, var(--photo-deep), #6d8f3a 50%, #d04868); }
  .photo--lawn { background: linear-gradient(170deg, #3b6a24, #8fb84a 60%, #5a3a2a); }
  .photo--parterre { background: linear-gradient(140deg, #5b9e38, #6a4a8c 55%, #4f8c2e); }
  .photo--grass { background: linear-gradient(170deg, #5f7d2a, var(--photo-light) 60%, #c7e06a); }

  .band {
    position: absolute; left: 0; right: 0; bottom: 0;
    background: linear-gradient(180deg, var(--band-light), var(--band-dark));
    border-top: 3px solid var(--card-black);
    box-shadow: 0 -6px 0 var(--leaf-green);
    color: var(--band-text);
    text-align: center;
    display: flex; align-items: center; justify-content: center;
  }
  .band--front { height: 92px; font-size: 15px; line-height: 1.4; padding: 0 20px; }
  .band--back { height: 140px; font-size: 19px; line-height: 1.35; padding: 0 36px; }

  /* Back */
  .back-header { padding: 70px 30px 0 0; display: flex; justify-content: flex-end; }
  .service-list {
    list-style: none;
    margin: 40px 0 0 46px;
    color: var(--leaf-green);
    font-size: 19px; line-height: 1.42;
  }
  .service-list li { display: flex; align-items: center; gap: 12px; }
  .service-list svg { flex: none; }
</style>
</head>
<body>
<main class="stage">

  <section class="postcard postcard--front" aria-label="Postcard front">
    <header class="front-header">
      <div class="brand">
        <span class="brand__dot"></span>
        <span class="brand__name">Fernvale<br>Landscapes</span>
      </div>
      <address class="contact" style="font-style:normal">
        Fernvale Landscapes<br>Marcus<br>0400 182
      </address>
    </header>
    <div class="rule"></div>
    <div class="photo-grid">
      <div class="photo photo--garden" role="img" aria-label="Photo of a terraced flower garden with winding lawn paths"></div>
      <div class="photo photo--trees" role="img" aria-label="Photo of a lawn with purple-leaved ornamental trees"></div>
      <div class="photo photo--steps" role="img" aria-label="Photo of garden steps lined with pink flowering shrubs"></div>
      <div class="photo photo--lawn" role="img" aria-label="Photo of a shaded garden with tree trunks and green lawn"></div>
      <div class="photo photo--parterre" role="img" aria-label="Photo of a clipped hedge parterre with purple planting"></div>
      <div class="photo photo--grass" role="img" aria-label="Close photo of tall ornamental grass"></div>
    </div>
    <p class="band band--front">we apologise for any disturbance you may incur<br>while we are working on your neighbours property</p>
  </section>

  <section class="postcard postcard--back" aria-label="Postcard back">
    <header class="back-header">
      <div class="brand">
        <span class="brand__dot"></span>
        <span class="brand__name">Fernvale<br>Landscapes</span>
      </div>
    </header>
    <ul class="service-list">
      <li><svg width="12" height="10" viewBox="0 0 12 10"><circle cx="6" cy="5" r="4" fill="var(--leaf-green)"/></svg>Design</li>
      <li><svg width="12" height="10" viewBox="0 0 12 10"><circle cx="6" cy="5" r="4" fill="var(--leaf-green)"/></svg>Paving and Concreting styles</li>
      <li><svg width="12" height="10" viewBox="0 0 12 10"><circle cx="6" cy="5" r="4" fill="var(--leaf-green)"/></svg>Pool Copings</li>
      <li><svg width="12" height="10" viewBox="0 0 12 10"><circle cx="6" cy="5" r="4" fill="var(--leaf-green)"/></svg>Retaining Walls</li>
      <li><svg width="12" height="10" viewBox="0 0 12 10"><circle cx="6" cy="5" r="4" fill="var(--leaf-green)"/></svg>Plant Supply</li>
      <li><svg width="12" height="10" viewBox="0 0 12 10"><circle cx="6" cy="5" r="4" fill="var(--leaf-green)"/></svg>Decking</li>
      <li><svg width="12" height="10" viewBox="0 0 12 10"><circle cx="6" cy="5" r="4" fill="var(--leaf-green)"/></svg>Pergolas</li>
      <li><svg width="12" height="10" viewBox="0 0 12 10"><circle cx="6" cy="5" r="4" fill="var(--leaf-green)"/></svg>Water Features</li>
      <li><svg width="12" height="10" viewBox="0 0 12 10"><circle cx="6" cy="5" r="4" fill="var(--leaf-green)"/></svg>Irrigation</li>
      <li><svg width="12" height="10" viewBox="0 0 12 10"><circle cx="6" cy="5" r="4" fill="var(--leaf-green)"/></svg>Instant Turf</li>
      <li><svg width="12" height="10" viewBox="0 0 12 10"><circle cx="6" cy="5" r="4" fill="var(--leaf-green)"/></svg>Synthetic Turf Surfaces</li>
      <li><svg width="12" height="10" viewBox="0 0 12 10"></svg>and more...</li>
    </ul>
    <p class="band band--back">While we are in your area we'd like to offer you a 10% discount on any of our landscaping services</p>
  </section>

</main>
</body>
</html>
```